High End Personalized Functional Medicine in Women's Health

We are adding new and exciting personalized medicine services to our Women's Health Care practice focusing on health optimization and anti-aging as well as hormone replacement therapy and need a high end brochure to educate patients about these services. We would like to see a zen-like design that has feminine appeal. Our office colors are vibrant but soothing. We have utilized the concepts of feng shui to optimize our positive energy. The exterior of the building is peach and cream and these colors would blend with that energy The final design should communicate a sense that you can take control of your health and aging.

Target Market(s)

Females age 35-65 with annual income >$75000/year

Industry/Entity Type

Health And Wellness

Logo Text

Bright Path is the company name. Our sister company is Corva Ridge Ob/Gyn

Font styles to use
Serif

Colors

Designer to choose colors to be used in the design.

Requirements
Must have
• My project must have clean lines. I like a strong feminine appearance, not a fluffy curvy feminine look. Professional appearance, Brochure would be on thicker card stock. A strong front page that makes you want to open the brochure
Nice to have
• Eye catching photos that complement our message . I am not tied to the peach and cream color recommendation, but find those colors feminine but not so cliche as pinks and purples.
Should not have
• frilly design

```html
<!DOCTYPE html>
<html lang="en">
<head>
<meta charset="utf-8">
<title>Bright Path Functional Medicine – Brochure</title>
<link rel="stylesheet" href="https://fonts.googleapis.com/css2?family=Libre+Baskerville:ital,wght@0,400;0,700;1,400&family=Lora:ital,wght@0,400;0,600;1,400&display=swap">
<style>
:root{
  --canvas:#e9e9eb;
  --paper:#fbfbfa;
  --peach:#eaae86;
  --peach-soft:#f3d2bb;
  --ink:#3a3a3a;
  --ink-soft:#6d6d6d;
  --stone:#a8a8a2;
  --photo-light:#e6e7e6;
  --photo-skin:#edd7c6;
  --photo-blue:#9fc8de;
  --bar:#3c3c3c;
}
*{box-sizing:border-box;margin:0;padding:0}
html,body{width:1200px;height:2700px;overflow:hidden}
body{background:var(--canvas);font-family:"Lora",serif;color:var(--ink);position:relative}

.sheet{position:absolute;background:var(--paper);box-shadow:0 14px 30px rgba(0,0,0,.12);overflow:hidden}

/* ---------- front cover ---------- */
.cover{width:600px;height:800px;position:relative;background:var(--paper)}
.cover-photo{position:absolute;left:0;top:0;width:600px;height:430px;
  background:linear-gradient(160deg,var(--photo-light) 0%,#f1eeeb 40%,var(--photo-skin) 70%,var(--photo-blue) 100%)}
.cover-tag{position:absolute;left:110px;top:0;width:300px;height:120px;background:var(--stone);
  display:flex;align-items:center;justify-content:center}
.cover-tag span{font-family:"Libre Baskerville",serif;font-weight:700;color:#fff;font-size:30px}
.cover-title{position:absolute;left:0;right:0;top:500px;text-align:center;font-family:"Libre Baskerville",serif;line-height:1}
.cover-title .brand{display:block;color:var(--peach);font-size:58px;letter-spacing:1px}
.cover-title .line{display:block;color:var(--ink);font-size:44px;margin-top:8px}
.cover-title .line.small{font-size:34px;margin-top:6px}
.cover-url{position:absolute;left:0;right:0;top:720px;text-align:center;font-size:16px;color:var(--ink-soft)}

/* ---------- outer spread ---------- */
.scaled{transform:scale(.8);transform-origin:0 0}
.back{width:480px;height:640px;position:absolute;left:0;top:0;background:var(--paper);border-right:1px solid #e2e2e2}
.family-photo{position:absolute;left:40px;top:230px;width:190px;height:130px;border:4px solid var(--peach);
  background:linear-gradient(180deg,#b9c2a6,#8e9a7c 60%,#6f7f93)}
.bio{position:absolute;left:250px;top:220px;width:200px}
.bio h3{font-family:"Libre Baskerville",serif;font-size:12px;margin-bottom:6px}
.bio p{font-size:9px;line-height:1.45;color:var(--ink-soft)}
.contact{position:absolute;left:0;right:0;top:430px;text-align:center}
.contact .brand{font-family:"Libre Baskerville",serif;font-weight:700;color:var(--peach);font-size:22px}
.contact h4{font-family:"Libre Baskerville",serif;font-size:15px;margin:8px 0 10px}
.contact .row{font-size:10px;color:var(--ink-soft);margin-top:6px}
.icon-dot{display:block;margin:8px auto 2px}
.contact .url{font-size:12px;margin-top:18px;color:var(--ink)}

/* ---------- inner spread ---------- */
.page{position:absolute;top:0;width:520px;height:700px;background:var(--paper)}
.page-left{left:0;border-right:1px solid #e0e0e0}
.page-right{left:520px}
.top-band{position:absolute;left:0;top:0;width:100%;height:14px;background:var(--peach)}
.lead{position:absolute;left:36px;top:38px;width:450px;font-family:"Libre Baskerville",serif;font-weight:700;font-size:18px;line-height:1.3}
.body{font-size:9px;line-height:1.5;color:var(--ink-soft)}
.intro{position:absolute;left:36px;top:140px;width:450px}
.quote{position:absolute;left:36px;top:222px;width:450px}
.quote h5{font-size:10px;font-weight:600;color:var(--ink);margin-bottom:3px}
.quote p{font-style:italic}
.framed{position:absolute;border:4px solid var(--peach);background:linear-gradient(160deg,#f4e1d3,#d8c4b8)}
.photo-a{left:36px;top:300px;width:210px;height:150px}
.photo-b{left:280px;top:270px;width:200px;height:130px}
.subhead{font-family:"Libre Baskerville",serif;font-weight:700;font-size:11px;color:var(--peach);margin-bottom:4px;line-height:1.3}
.block-why{position:absolute;left:36px;top:470px;width:220px}
.block-who{position:absolute;left:280px;top:415px;width:205px}
.block-symptoms{position:absolute;left:36px;top:570px;width:450px}
.page-brand{position:absolute;left:36px;top:650px;font-family:"Libre Baskerville",serif;font-weight:700;font-size:20px;color:var(--peach)}

.face-row{position:absolute;left:40px;top:0;width:480px;height:140px;display:flex}
.face-row div{flex:1}
.face-row div:nth-child(1){background:linear-gradient(180deg,#f3ebe5,#e9d3c4)}
.face-row div:nth-child(2){background:linear-gradient(180deg,#efe2d8,#dfc3af)}
.face-row div:nth-child(3){background:linear-gradient(180deg,#8fbfc2,#cfe0df)}
.face-row div:nth-child(4){background:linear-gradient(180deg,#f6eee9,#e8cfbf)}
.col{position:absolute;width:210px}
.col-1{left:36px;top:170px}
.col-2{left:275px;top:170px}
.item{display:flex;gap:8px;margin-bottom:22px}
.item svg{flex:none}
.item h6{font-family:"Libre Baskerville",serif;font-size:11px;color:var(--peach);margin-bottom:3px}
.item h6.dark{color:var(--ink)}
.plain{margin-top:10px}
.plain h6{font-family:"Libre Baskerville",serif;font-size:11px;color:var(--ink);margin-bottom:4px}
.url-bar{position:absolute;right:30px;top:640px;background:var(--bar);color:#fff;font-size:10px;padding:6px 14px}
</style>
</head>
<body>

<!-- front cover -->
<section class="sheet" style="left:300px;top:50px;width:600px;height:800px">
  <div class="cover">
    <div class="cover-photo" role="img" aria-label="Photo of a woman receiving a facial treatment from a clinician in gloves"></div>
    <div class="cover-tag"><span>Bright Path</span></div>
    <h1 class="cover-title">
      <span class="brand">BRIGHT PATH</span>
      <span class="line">FUNCTIONAL</span>
      <span class="line small">MEDICINE</span>
    </h1>
    <p class="cover-url">www.brightpathfunctionalmedicine.com</p>
  </div>
</section>

<!-- outer spread: back + front -->
<section class="sheet" style="left:120px;top:1000px;width:960px;height:640px">
  <div class="back">
    <div class="family-photo" role="img" aria-label="Family photo of the doctor outdoors"></div>
    <div class="bio">
      <h3>Dr. Varga with family</h3>
      <p>Dr. Varga specializes in women's health and has over 22 years of experience. She is an expert in bio-identical hormone therapy and has been a pellet provider for over ten years.</p>
    </div>
    <div class="contact">
      <div class="brand">Bright Path</div>
      <h4>Contact Us</h4>
      <svg class="icon-dot" width="16" height="16" viewBox="0 0 16 16"><circle cx="8" cy="8" r="8" fill="#3a3a3a"/><path d="M5.5 4.5l1.5 1.5-.8 1c.5 1 1.3 1.8 2.3 2.3l1-.8 1.5 1.5-1 1c-2.8-.3-5.2-2.7-5.5-5.5z" fill="#fff"/></svg>
      <div class="row">555-214-0387</div>
      <svg class="icon-dot" width="16" height="16" viewBox="0 0 16 16"><circle cx="8" cy="8" r="8" fill="#3a3a3a"/><rect x="4" y="5.5" width="8" height="5.5" fill="none" stroke="#fff" stroke-width="1"/><path d="M4 5.5l4 3 4-3" fill="none" stroke="#fff" stroke-width="1"/></svg>
      <div class="row">info@brightpathfunctionalmedicine.com</div>
      <div class="url">www.brightpathfunctionalmedicine.com</div>
    </div>
  </div>
  <div style="position:absolute;left:480px;top:0;width:480px;height:640px;overflow:hidden">
    <div class="cover scaled">
      <div class="cover-photo" role="img" aria-label="Photo of a woman receiving a facial treatment from a clinician in gloves"></div>
      <div class="cover-tag"><span>Bright Path</span></div>
      <div class="cover-title">
        <span class="brand">BRIGHT PATH</span>
        <span class="line">FUNCTIONAL</span>
        <span class="line small">MEDICINE</span>
      </div>
      <p class="cover-url">www.brightpathfunctionalmedicine.com</p>
    </div>
  </div>
</section>

<!-- inner spread -->
<section class="sheet" style="left:80px;top:1920px;width:1040px;height:700px">
  <article class="page page-left">
    <div class="top-band"></div>
    <h2 class="lead">Functional medicine's aim is to heal the physical body in order to engage in our life purpose of connection and emotional and spiritual growth.</h2>
    <p class="body intro">Dr. Elena Varga specializes in women's health and has over 22 years of experience. She is an expert in bio-identical hormone replacement therapy and has been a leading pellet practitioner for over ten years. Her practice focuses on nutrition, stress, sleep and lifestyle change, treating the root cause of symptoms rather than masking them with medication alone.</p>
    <div class="quote">
      <h5>What do patients have to say about their experience with Dr. Varga?</h5>
      <p class="body">“Dr. Varga listened, tested and found answers. I feel like myself again.” — patient</p>
    </div>
    <div class="framed photo-a" role="img" aria-label="Portrait of a woman showing before and after skin renewal"></div>
    <div class="framed photo-b" role="img" aria-label="Portrait of a smiling woman with hands at her face"></div>
    <div class="block-who">
      <h4 class="subhead">Who else should consider a functional medicine visit?</h4>
      <p class="body">Anyone who wants to prevent illness, age with strength and feel their best. Our plans are built around your labs, goals and daily life.</p>
    </div>
    <div class="block-why">
      <h4 class="subhead">Why should you consider a functional medicine visit?</h4>
      <p class="body">You are tired of feeling tired. You want answers, not another prescription. A functional visit looks at your whole story to find what is out of balance.</p>
    </div>
    <div class="block-symptoms">
      <h4 class="subhead">What Symptoms Do We Treat?</h4>
      <p class="body">Weight gain, fatigue, low mood and poor sleep often share a root cause. When hormones, gut and stress are out of balance, the body struggles to heal.</p>
    </div>
    <div class="page-brand">Bright Path</div>
  </article>

  <article class="page page-right">
    <div class="face-row" role="img" aria-label="Row of four beauty portraits of women">
      <div></div><div></div><div></div><div></div>
    </div>
    <div class="col col-1">
      <div class="item">
        <svg width="22" height="22" viewBox="0 0 22 22"><circle cx="11" cy="11" r="11" fill="#3a3a3a"/><circle cx="11" cy="11" r="5" fill="none" stroke="#fff" stroke-width="1.2"/></svg>
        <div><h6>Fatigue</h6><p class="body">Adrenal and thyroid imbalance can leave you drained. We test cortisol and thyroid levels and restore steady energy.</p></div>
      </div>
      <div class="item">
        <svg width="22" height="22" viewBox="0 0 22 22"><circle cx="11" cy="11" r="11" fill="#3a3a3a"/><path d="M7 11h8M11 7v8" stroke="#fff" stroke-width="1.2"/></svg>
        <div><h6>Female Hormone Imbalance</h6><p class="body">Optimizing hormonal balance is our specialty. We help with hot flashes, night sweats, low libido and weight change.</p></div>
      </div>
      <div class="plain">
        <h6>What can I expect from my first visit?</h6>
        <p class="body">During your initial consultation we review your history, goals and labs. You leave with a clear, personal plan to restore balance and feel well.</p>
      </div>
    </div>
    <div class="col col-2">
      <div class="item">
        <svg width="22" height="22" viewBox="0 0 22 22"><circle cx="11" cy="11" r="11" fill="#3a3a3a"/><path d="M7 13c1.5-2 6.5-2 8 0" fill="none" stroke="#fff" stroke-width="1.2"/></svg>
        <div><h6>Depression</h6><p class="body">We look past symptoms to nutrient gaps, inflammation and hormone shifts that affect mood.</p></div>
      </div>
      <div class="item">
        <svg width="22" height="22" viewBox="0 0 22 22"><circle cx="11" cy="11" r="11" fill="#3a3a3a"/><rect x="7" y="7" width="8" height="8" fill="none" stroke="#fff" stroke-width="1.2"/></svg>
        <div><h6>GI problems</h6><p class="body">The gut is the center of health. We treat bloating, reflux and food sensitivity at the source.</p></div>
      </div>
      <div class="plain">
        <h6>What are your treatment protocols based on?</h6>
        <p class="body">Treatment protocols are based on advanced lab testing, nutrition, bio-identical hormones and lifestyle support tailored to you.</p>
      </div>
    </div>
    <div class="url-bar">www.brightpathfunctionalmedicine.com</div>
  </article>
</section>

</body>
</html>
```